Raw Food & Health Coach Needs a Clutch Coupon

I need a clutch coupon for a raw food & health coaching business based in Washington, DC called Cora Penwick, LLC. I help ladies and gents on the go who want to support their bodies to stay healthy or prevent/correct disease so they can live extraordinary lives while deeply serving the world. My services include individual coaching, (online) group coaching, and corporate wellness coaching.

I would like to create a clutch coupon to give to referral partners who in turn will give them to their clients. So far I have two referral partners in mind: Marcus Elvey Salon & Spa; and Colon Hydrotherapist Wendy Tasbrook.

Marcus Elvey Salon & Spa will be having an event on Thursday, September 12, 2013, during which time their clients who get a hair cut will receive a complimentary Velunique (hair) Treatment & a complimentary Radiant Through and Through Planning Hour with me.

I would like to see designs that use 2-4 colors, including a bit of green. The final design should communicate beauty/health from the inside out and boundless energy to enjoy an extraordinary life. It should be natural yet elegant/classy.

Designers are currently working on my business logo. The logo design project has not yet been completed. Once it completes, I will send the logo design to you and request that you incorporate the logo into your coupon design.

IMPORTANT: I need to select a winning design on Wed, Sept 11, 2013, and get the source files from the designer within 24 hours (before Thursday, Sept 12 MORNING); so that I have time to adjust any text and take it to the printer in order to distribute the coupon later that afternoon. I will need the source files urgently (within the next 24 hours).

Then after the event the designer will make the changes on the design for me incorporating my logo for use with multiple referral partners. I will approve the Payment when I have finalized the design

To repeat, I must have the winning design on September 11 (or Sept 12 morning at the latest).

IMPORTANT: Refer to uploaded Referral Partner Clutch Coupon SAMPLE to give you an idea of the layout I'd like, but PLEASE don't let it stifle YOUR creativity.
Updates

The focus should be on the Free Radiant Through and Through Planning Hour, not on me.

 

I think I’d prefer a white background and black text, unless you can convince me otherwise by showing me a beautiful design.

 

Ensure there is space between paragraphs.

 

Somehow differentiate my free gift (Wellbeing Guard Starter Kit), phone and URL at the bottom on the back. While it would be nice to include my free gift, I may have to leave out if it won’t fit on the coupon.

Target Market(s)

The audience is busy, heart-centered/socially responsible professional men and women on the go who hardly have time for self-care, but who will pay for holistic services (alternative therapies) to enhance their beauty/health so that they can perform their best while deeply serving the world without getting sick or having to endure toxic therapies like surgery, chemotherapy, radiation, and pills.

Industry/Entity Type

Printer

Requirements
Must have
• 2-4 colors, including a little green

Dimensions: approx. 2.25 inches x 5.25 inches.

Text from the uploaded file. Note: I'm not sure if all the text I've provided will fit nicely on the back of the coupon. If no then please increase the dimensions as little as possible.

The front of the coupon designed horizontally, and the back designed vertically.
Nice to have
• I'm open to your using illustrations or photos of the raw food and/or lifestyle tools that I use with clients in my business, such as green juice, (leafy) green veggies, cucumbers, lemons, berries, green smoothies, superfoods, movement/exercise, self-care...

I also like the idea of including a face in the design. When I’ve surveyed in the past people have related better to a face than just to a bowl of veggies or fruit.
Should not have
• the colors orange or red, or florescent colors.

```html
<!DOCTYPE html>
<html lang="en">
<head>
<meta charset="utf-8">
<title>Cora Penwick, LLC – Clutch Coupon</title>
<link rel="stylesheet" href="https://fonts.googleapis.com/css2?family=Cinzel:wght@400;600&family=Hind:wght@400;500;600&family=Raleway:wght@300;400&display=swap">
<style>
  :root {
    --stage: #000000;
    --cream: #fbf7d2;
    --cream-soft: #fffdf0;
    --card-edge: #d8d6c4;
    --ink: #3a3a3a;
    --ink-soft: #555555;
    --brown: #5a3414;
    --brown-soft: #7a5126;
    --green: #7aa63a;
    --link: #e0208a;
    --qa-faint: rgba(150, 140, 90, 0.22);
    --white: #ffffff;
  }
  * { box-sizing: border-box; margin: 0; padding: 0; }
  html, body { width: 1200px; height: 1000px; overflow: hidden; background: var(--stage); }
  .canvas { position: relative; width: 1200px; height: 1000px; }

  /* Back of coupon */
  .coupon-back {
    position: absolute; left: 82px; top: 118px; width: 310px; height: 720px;
    border-radius: 9px; border: 1px solid var(--card-edge);
    background: linear-gradient(180deg, var(--cream) 0%, var(--cream-soft) 55%, var(--cream) 100%);
    font-family: "Hind", Arial, sans-serif; color: var(--ink);
    padding: 0 20px 0 28px; overflow: hidden;
  }
  .qa-mark {
    position: absolute; left: 52px; top: -6px;
    font-family: "Cinzel", Georgia, serif; font-size: 96px; font-weight: 400;
    color: var(--qa-faint); letter-spacing: -4px; line-height: 1;
  }
  .back-title {
    position: relative; margin-top: 16px; text-align: center;
    font-family: "Cinzel", Georgia, serif; font-weight: 600; font-size: 20.5px;
    line-height: 23px; color: #3f3a2c; letter-spacing: 0.2px;
  }
  .back-copy p { font-size: 9.4px; line-height: 11.5px; color: var(--ink-soft); }
  .back-copy p + p { margin-top: 11.5px; }
  .back-copy .intro { margin-top: 4px; }
  .back-copy h3 { font-size: 11.5px; font-weight: 600; color: var(--ink); margin-top: 12px; line-height: 12px; }
  .back-copy h4 { font-size: 9.4px; font-weight: 600; color: var(--ink); margin-top: 12px; line-height: 11px; }
  .benefit-list { list-style: none; margin-left: 12px; margin-top: 1px; }
  .benefit-list li { font-size: 9.4px; line-height: 11.4px; color: var(--ink-soft); }
  .benefit-list li::before { content: "•"; margin-right: 4px; }

  .booking-row { position: absolute; left: 46px; top: 540px; display: flex; gap: 12px; }
  .portrait {
    width: 60px; height: 72px; border: 2px solid var(--white);
    background: linear-gradient(160deg, #8a5a3e 0%, #c49478 50%, #5e3a26 100%);
  }
  .booking-text {
    margin-top: 11px; font-family: "Raleway", Arial, sans-serif; font-weight: 300;
    font-size: 11.5px; line-height: 13.5px; color: #555;
  }
  .booking-text a { color: var(--link); text-decoration: none; font-weight: 400; }

  .gift-box {
    position: absolute; left: 32px; top: 628px; width: 254px; height: 64px;
    border: 1px solid #cfcdb8; border-radius: 7px; text-align: center; padding-top: 5px;
    font-size: 9.2px; line-height: 11.5px; color: var(--ink-soft);
  }
  .gift-box strong { display: block; font-size: 11.5px; font-weight: 600; color: var(--ink); line-height: 14px; margin-bottom: 1px; }
  .gift-box b { font-weight: 600; color: var(--ink); }

  /* Front of coupon */
  .coupon-front {
    position: absolute; left: 424px; top: 310px; width: 720px; height: 309px;
    border-radius: 9px; border: 1px solid var(--card-edge); overflow: hidden;
  }
  .front-bg { position: absolute; inset: 0; }
  .brand-dot {
    position: absolute; left: 20px; top: 36px; width: 112px; height: 112px; border-radius: 50%;
    background: radial-gradient(circle at 40% 40%, #a9cd55 0%, var(--green) 55%, #4e7d2a 100%);
  }
  .brand-block { position: absolute; left: 142px; top: 52px; width: 230px; }
  .brand-name { font-family: "Raleway", Arial, sans-serif; font-size: 15.5px; color: var(--brown-soft); font-weight: 400; }
  .brand-name small { font-size: 11px; }
  .brand-role { font-family: "Hind", Arial, sans-serif; font-size: 9.6px; color: var(--brown-soft); letter-spacing: 0.2px; }
  .brand-rule { height: 1px; background: var(--brown-soft); margin-top: 5px; width: 229px; }
  .offer-title {
    position: absolute; left: 142px; top: 100px; width: 250px;
    font-family: "Hind", Arial, sans-serif; font-weight: 600; font-size: 21.5px; line-height: 28.8px;
    color: var(--brown); white-space: nowrap;
  }
  .offer-side { position: absolute; left: 489px; top: 42px; width: 220px; font-family: "Raleway", Arial, sans-serif; }
  .offer-value { font-weight: 300; font-size: 18.5px; line-height: 23px; color: #666; margin-left: 6px; }
  .offer-booking { margin-top: 30px; font-weight: 400; font-size: 12.5px; line-height: 15.5px; color: #666; }
  .offer-booking a { color: var(--link); text-decoration: none; }
  .partner { position: absolute; left: 520px; top: 212px; width: 124px; text-align: center; }
  .partner-label { font-family: "Raleway", Arial, sans-serif; font-size: 10px; color: #9a9a9a; }
  .partner-name {
    margin-top: 10px; font-family: "Raleway", Arial, sans-serif; font-weight: 400;
    font-size: 14px; line-height: 16px; color: #7c8794; letter-spacing: 1px; text-transform: uppercase;
  }
</style>
</head>
<body>
<main class="canvas">

  <section class="coupon-back" aria-label="Coupon back">
    <div class="qa-mark" aria-hidden="true">Q&amp;A</div>
    <h2 class="back-title">What is raw food &amp;<br>health coaching?</h2>
    <div class="back-copy">
      <p class="intro">Raw food coaching helps you go or stay raw to the level that you truly desire.</p>
      <p>Health couching helps you connect the dots between what you eat and how you feel. You'll know how to detoxify your body, boost your immune system, multiply your energy, improve your mood, gravitate to the perfect body weight for you, and delight in what you eat like never before – without restriction.</p>
      <h3>Who benefits from this work?</h3>
      <p>Ladies and gents on the go who want to enable their bodies to prevent or correct disease and create abundant energy so they can live extraordinary lives while deeply serving the world.</p>
      <p>Raw food is literally for everyone, but the degree to which someone goes raw and for what duration is a very personal decision. This is about what works for you, what feels right for you and what get you to where you want to be.</p>
      <h4>Generally speaking, raw food is great for anyone who wants to…</h4>
      <ul class="benefit-list">
        <li>Correct or prevent a serious disease</li>
        <li>Look and/or feel better</li>
        <li>Look/feel 10 years younger</li>
        <li>Fit into their skinny jeans without dieting</li>
        <li>Double their energy</li>
        <li>Reduce their cravings</li>
        <li>Detox their body</li>
        <li>Think more clearly</li>
        <li>Get a lot done without having a lot of time</li>
        <li>Feel happier</li>
      </ul>
      <h4>What happens in the initial strategy session?</h4>
      <p>This 30 minute phone call is a time to discuss your unique health challenge(s) and desires. I guarantee you'll walk away with at least 1 aha about why you're stuck and more clarity about what it'll take to put you on the fast track to where you want to go.</p>
    </div>

    <div class="booking-row">
      <div class="portrait" role="img" aria-label="Portrait photo of the coach Cora Penwick"></div>
      <p class="booking-text">To book your complimentary<br>strategy session<br>simply go to: <a href="#">http://go.link/RTT4h</a></p>
    </div>

    <div class="gift-box">
      <strong>Afraid of getting cancer?</strong>
      Decide To Get Healthy Because It's Time…<br>
      Get Your Free Wellbeing Guard Starter Kit At<br>
      corapenwick.com <b>TODAY!</b>
    </div>
  </section>

  <section class="coupon-front" aria-label="Coupon front">
    <svg class="front-bg" width="720" height="309" viewBox="0 0 720 309" aria-hidden="true">
      <defs>
        <radialGradient id="creamGlow" cx="0.3" cy="0.5" r="0.7">
          <stop offset="0" stop-color="#fffef4"/>
          <stop offset="1" stop-color="#f7f1be"/>
        </radialGradient>
        <linearGradient id="goldBand" x1="0" y1="0" x2="0" y2="1">
          <stop offset="0" stop-color="#c98f2a"/>
          <stop offset="0.5" stop-color="#f5d27a"/>
          <stop offset="1" stop-color="#c98f2a"/>
        </linearGradient>
      </defs>
      <rect width="720" height="309" fill="url(#creamGlow)"/>
      <path d="M404 0 Q474 154 408 309 L720 309 L720 0 Z" fill="#ffffff"/>
      <path d="M384 0 Q442 154 386 309 L408 309 Q474 154 404 0 Z" fill="url(#goldBand)"/>
    </svg>

    <div class="brand-dot" aria-hidden="true"></div>
    <div class="brand-block">
      <p class="brand-name">cora penwick, <small>LLC</small></p>
      <p class="brand-role">RAW FOOD &amp; HEALTH COACH</p>
      <div class="brand-rule"></div>
    </div>
    <h1 class="offer-title">Free Radiant Through<br>and Through Planning<br>Hour with Certified<br>Raw Food &amp; Health<br>Coach</h1>

    <div class="offer-side">
      <p class="offer-value">30 minutes focused<br>entirely on you<br>(a $50 value, free)</p>
      <p class="offer-booking">To book your complimentary<br>strategy session<br>simply go to: <a href="#">http://go.link/RTT4h</a></p>
    </div>

    <div class="partner">
      <p class="partner-label">Compliments Of</p>
      <p class="partner-name">Marcus Elvey<br>Salon &amp; Spa</p>
    </div>
  </section>

</main>
</body>
</html>
```